Fashion clothing business needs a label, swing tag and business card.

Independent womenswear label called "Tessa Wrenly".
I'd like a design for a woven label to go on the clothes, a swing tag and business card design. The design should be simple, modern but timeless. Its a small business, made locally in Melbourne, Australia, produces quality garments for everyday wear using beautiful fabrics.

Reason: just waiting for a few others to submit their designs.

Target Market(s)

30+ ladies, who want quality everyday wear, who don't necessarily follow trends. They can be a bit edgy and willing to take a risk with something different.

Industry/Entity Type

Clothing

Font styles to use
Other font styles liked:
• I dont mind the typewriter font, but can it look modern? happy for you to choose.

Requirements
Should not have
• A difficult shape swing tag - as it might be more expensive for me to get printed and cut.

```html
<!DOCTYPE html>
<html lang="en">
<head>
<meta charset="utf-8">
<title>Tessa Wrenly — Swing Tag</title>
<link rel="stylesheet" href="https://fonts.googleapis.com/css2?family=Fira+Sans:wght@500;600&display=swap">
<style>
  :root {
    --page: #ffffff;
    --tag-card: #d4d4d6;
    --string: #ececec;
    --eyelet-ring: #ebebeb;
    --ink: #111111;
    --rule: #6e6e70;
  }
  html, body {
    margin: 0;
    padding: 0;
    width: 799px;
    height: 1200px;
    overflow: hidden;
    background: var(--page);
  }
  .swing-tag {
    display: block;
    width: 799px;
    height: 1200px;
  }
  .tag-card { fill: var(--tag-card); }
  .hang-string {
    fill: none;
    stroke: var(--string);
    stroke-width: 5;
    stroke-linecap: round;
  }
  .eyelet-ring { fill: var(--eyelet-ring); }
  .eyelet-hole { fill: var(--page); }
  .field-label {
    font-family: "Fira Sans", sans-serif;
    font-weight: 600;
    font-size: 25px;
    letter-spacing: 0.4px;
    fill: var(--ink);
  }
  .field-rule {
    stroke: var(--rule);
    stroke-width: 1.4;
  }
  .brand-mark { fill: var(--ink); }
  .brand-name {
    font-family: "Fira Sans", sans-serif;
    font-weight: 600;
    font-size: 51px;
    fill: var(--ink);
  }
  .web-address {
    font-family: "Fira Sans", sans-serif;
    font-weight: 500;
    font-size: 21px;
    letter-spacing: 3.8px;
    fill: var(--ink);
  }
</style>
</head>
<body>
<svg class="swing-tag" viewBox="0 0 799 1200" xmlns="http://www.w3.org/2000/svg">
  <!-- card -->
  <rect class="tag-card" x="111" y="429" width="606" height="770" rx="46" ry="46"/>

  <!-- hanging string -->
  <path class="hang-string"
        d="M410 428 C 500 330, 640 220, 642 90 C 644 30, 590 20, 560 60 C 500 140, 465 260, 455 370 C 450 430, 450 480, 440 505 C 430 525, 400 525, 392 505"/>

  <!-- eyelet -->
  <ellipse class="eyelet-ring" cx="405" cy="560" rx="61" ry="78"/>
  <ellipse class="eyelet-hole" cx="405" cy="560" rx="47" ry="63"/>
  <path class="hang-string" d="M392 505 C 400 535, 430 540, 440 505"/>

  <!-- detail fields -->
  <g class="tag-fields">
    <text class="field-label" x="256" y="741">Size:</text>
    <line class="field-rule" x1="314" y1="740" x2="581" y2="740"/>
    <text class="field-label" x="256" y="804">style:</text>
    <line class="field-rule" x1="327" y1="803" x2="581" y2="803"/>
    <text class="field-label" x="256" y="867">Price:</text>
    <line class="field-rule" x1="327" y1="866" x2="581" y2="866"/>
  </g>

  <!-- brand -->
  <circle class="brand-mark" cx="425" cy="1045" r="60"/>
  <text class="brand-name" x="425" y="1164" text-anchor="middle">Tessa Wrenly</text>

  <!-- vertical web address -->
  <text class="web-address" transform="translate(678 1162) rotate(-90)">www.tessawrenly.com</text>
</svg>
</body>
</html>
```